Starter & Alternator business needs a website

update: very good designs submitted so far. also need this to display well on mobile devices. not sure if wordpress or html/css is better for my needs.

Our existing website is vellumtorq.com and is need of total revamp. Need full design of a website for my business.

We sell and rebuild starters and alternators. Customers bring in the units and we rebuild them. Or we sell them brand new or rebuilt units we have in stock. We do not install units into vehicles like a mechanic would. We strictly rebuild starters and alternators in our shop, sell brand new units over the counter, and we do deliver occasionally as well. We do offer a line of Orvan batteries as well but that is only a small feature of the business.

I would like this website designed and coded. I can upload the files to my web host after completion. I can also add in and modify content like our background info, etc.

I have included an illustrator file that shows some of our signage and logo, etc. I have also included a radio commercial sample so you can get a little better feel for the business. A similar ad does run on the radio currently, slightly different and without the added sound effects.

Update: I do like using photos of real items(starters or alternators etc) for an icon, like a real alternator stock image for the alternator section icon, etc. Maybe incorporate our logo in that design as well. That looks nice as well and may aid in navigation.

For any other design elements, do what you think looks good. Our colors are red/white/blue as seen in the illustrator file. our building is painted with halbeck moray colors, ember gala red and deep tide for blue.

Here are some examples of rebuilders websites in other markets for reference:

https://quillmarauto.com/starter-alternator-rebuilding/

https://www.dunwickmotorworks.com/auto-repairs/alternator-starter-rebuilds.aspx

https://www.fjordvoltage.com/

https://www.pemberlowgx.com/

The website can have areas for: services and products offered, high output alternators, Orvan Batteries, troubleshooting tips, current specials, contact info and directions/map, etc. Whatever else you feel applies.

At some point I do want to be able to sell items directly online or at least have a secure section for customers to submit invoice payments, but that's not necessarily in scope for this project just something to keep in mind.

Target Market(s)

Mechanics and Managers in fleet shops, construction and marine industries, shipping trades. Also automobile owners who work on their own vehicles. We sell and rebuild starters and alternators for automobiles, heavy duty equipment, forklifts, traxlifts, man movers, ferrettes, loaders, large tractors and trucks, just about any engine, golf carts, generators, etc.

Industry/Entity Type

Automotive Part

Coding

Coded - Design and coding required

Number of Pages Required

5+ page

Font styles to use
Serif
Sans Serif

Colors
0255a3
ec1f27
ffffff

Requirements
Must have
• Should also display nicely on mobile phones. Highlight our specialty, "Starters & Alternators"

```html
<!DOCTYPE html>
<html lang="en">
<head>
<meta charset="utf-8">
<title>Starters &amp; Alternators</title>
<link rel="stylesheet" href="https://fonts.googleapis.com/css2?family=Montserrat:wght@500;600;700;800;900&family=Open+Sans:wght@400;600&display=swap">
<style>
:root{
  --blue:#0255a3;
  --navy:#1f2a5c;
  --red:#ec1f27;
  --white:#ffffff;
  --band:#3370b4;
  --grey-bg:#f4f4f4;
  --text:#555b66;
  --footer:#1f2128;
  --icon-bg:#e6e8f0;
}
*{margin:0;padding:0;box-sizing:border-box}
html,body{width:1200px;height:3484px;overflow:hidden}
body{position:relative;background:var(--white);font-family:"Open Sans",sans-serif;color:var(--text)}
.abs{position:absolute}

/* header */
.brand{left:89px;top:19px;display:flex;align-items:center;gap:12px}
.brand-badge{width:80px;height:80px;display:flex;align-items:center;justify-content:center;text-align:center;font-family:"Montserrat",sans-serif;font-weight:800;font-size:11px;line-height:14px;color:var(--navy)}
.brand-name{font-family:"Montserrat",sans-serif;font-weight:900;font-size:40px;line-height:40px;color:var(--navy)}
.info-label{font-family:"Montserrat",sans-serif;font-weight:700;font-size:15px;color:var(--blue)}
.info-value{font-family:"Montserrat",sans-serif;font-weight:600;font-size:18px;color:var(--red)}

/* nav */
.nav{left:0;top:122px;width:1200px;height:46px;background:var(--blue)}
.nav-search{left:828px;top:122px;width:372px;height:46px;background:var(--red);clip-path:polygon(14px 0,100% 0,100% 100%,0 100%)}
.nav-links{left:122px;top:122px;height:46px;display:flex;align-items:center;gap:36px;font-family:"Montserrat",sans-serif;font-weight:600;font-size:17px;color:var(--white)}
.search-text{left:868px;top:134px;font-size:15px;color:var(--white)}

/* hero */
.hero{left:0;top:168px;width:1200px;height:583px;background:linear-gradient(110deg,#5a8a2a 0%,#3d4a3a 28%,#6e7377 50%,#4a4d51 75%,#2f3236 100%)}
.hero-title{left:89px;top:330px;font-family:"Montserrat",sans-serif;font-weight:800;font-size:55px;line-height:64px;color:var(--white)}
.hero-sub{left:91px;top:405px;font-size:22px;color:var(--white)}
.btn{display:flex;align-items:center;gap:14px;background:var(--red);color:var(--white);font-family:"Montserrat",sans-serif;font-weight:600;font-size:19px;padding:0 16px;border-radius:3px}

/* services */
.section-title{width:1200px;left:0;text-align:center;font-family:"Montserrat",sans-serif;font-weight:800;font-size:40px;line-height:50px;color:var(--blue)}
.service{width:220px;text-align:center}
.service-icon{width:130px;height:118px;margin:0 auto;border-radius:50%;background:radial-gradient(circle,var(--white) 45%,var(--icon-bg) 46%,#c9cddd 100%)}
.service-name{margin-top:42px;font-family:"Montserrat",sans-serif;font-weight:700;font-size:21px;line-height:32px;color:var(--blue)}
.service-text{margin-top:30px;font-size:15px;line-height:27px}

/* about */
.about{left:0;top:1394px;width:1200px;height:525px;background:var(--band)}
.about-title{left:91px;top:1462px;font-family:"Montserrat",sans-serif;font-weight:800;font-size:40px;line-height:50px;color:var(--white)}
.about-text{left:91px;top:1538px;width:511px;font-size:17px;line-height:32.3px;color:var(--white);text-align:justify}
.about-photo{left:702px;top:1472px;width:406px;height:367px;background:linear-gradient(135deg,#5b5f63,#2b3a4a 55%,#1f6aa0)}

/* product */
.product-box{left:89px;top:2016px;width:418px;height:360px;border:2px solid #d8d8d8;box-shadow:0 0 6px rgba(0,0,0,.2);background:var(--white)}
.product-photo{left:130px;top:2066px;width:330px;height:250px;background:radial-gradient(ellipse at center,#b4b8bc 0%,#7f8489 50%,var(--white) 72%)}
.product-heading{left:543px;top:2008px;font-family:"Montserrat",sans-serif;font-weight:800;font-size:40px;line-height:50px;color:var(--blue)}
.product-name{left:543px;top:2083px;font-family:"Montserrat",sans-serif;font-weight:700;font-size:28px;line-height:36px;color:var(--red)}
.product-price{left:543px;top:2128px;font-family:"Montserrat",sans-serif;font-weight:800;font-size:42px;line-height:52px;color:var(--blue)}
.product-text{left:544px;top:2191px;width:532px;font-size:15px;line-height:27px;text-align:justify}

/* news */
.news{left:0;top:2476px;width:1200px;height:668px;background:var(--grey-bg)}
.news-intro{left:260px;top:2600px;width:680px;text-align:center;font-size:16px;line-height:28px}
.news-main{left:91px;top:2690px;width:491px;height:312px;background:linear-gradient(135deg,#6a6258,#3b3530 50%,#b83a30)}
.news-main-bar{left:91px;top:3002px;width:491px;height:94px;background:var(--red);color:var(--white)}
.news-main-title{position:absolute;left:16px;top:16px;font-family:"Montserrat",sans-serif;font-weight:700;font-size:23px}
.news-main-meta{position:absolute;left:18px;top:56px;font-size:16px}
.arrow-btn{position:absolute;top:50px;width:30px;height:30px;border-radius:50%;background:var(--white)}
.news-thumb{width:195px;height:192px}
.news-meta{font-size:14px;color:#444}
.news-title{font-family:"Montserrat",sans-serif;font-weight:700;font-size:22px;color:var(--blue)}
.news-text{width:291px;font-size:14px;line-height:22.5px;text-align:justify}
.read-more{font-family:"Montserrat",sans-serif;font-weight:700;font-size:16px;color:var(--red)}

/* footer */
.footer{left:0;top:3144px;width:1200px;height:340px;background:var(--footer)}
.f-title{left:89px;top:3217px;font-family:"Montserrat",sans-serif;font-weight:600;font-size:22px;color:var(--white)}
.f-input{left:89px;top:3268px;width:276px;height:36px;background:var(--white);border:2px solid #ccc}
.f-input span{position:absolute;left:8px;top:9px;font-size:13px;color:#222}
.f-sub{position:absolute;right:3px;top:3px;width:92px;height:26px;background:var(--red);color:var(--white);font-size:12px;text-align:center;line-height:26px}
.social{left:89px;top:3336px;display:flex;gap:12px}
.social i{width:20px;height:20px;border:1.5px solid var(--white);border-radius:50%}
.f-links{left:498px;top:3202px;font-size:17px;line-height:32.2px;color:var(--white)}
.f-address{left:683px;top:3202px;font-size:17px;line-height:32.2px;color:var(--white)}
.f-mark{left:964px;top:3236px;width:140px;text-align:center;font-family:"Montserrat",sans-serif;font-weight:800;font-size:17px;line-height:24px;color:var(--white)}
.copy{left:93px;top:3437px;font-size:15px;color:var(--white)}
.pay{left:590px;top:3438px;display:flex;gap:6px}
.pay i{width:34px;height:22px;border-radius:3px;background:#d7d9de}
.policy{left:992px;top:3442px;font-size:15px;color:var(--white);display:flex;gap:14px}
</style>
</head>
<body>

<!-- header -->
<div class="abs brand">
  <div class="brand-badge">VELLUM&shy;TORQ<br>REBUILDERS</div>
  <div class="brand-name">STARTERS &amp;<br>ALTERNATORS</div>
</div>
<div class="abs info-label" style="left:679px;top:36px">OUR HOURS OF OPERATION</div>
<div class="abs info-value" style="left:679px;top:64px">Mon-Fri 8-6 Pm,Sat 9 Am-2 Pm</div>
<div class="abs info-label" style="left:978px;top:36px">CALL US TODAY !</div>
<div class="abs info-value" style="left:978px;top:64px">555-014-2270</div>

<!-- nav -->
<div class="abs nav"></div>
<div class="abs nav-search"></div>
<nav class="abs nav-links">
  <span>&#9889; Home</span><span>About Us</span><span>Services</span><span>Our Product</span><span>Blog</span><span>Contact Us</span>
</nav>
<div class="abs search-text">Serach the Products</div>
<svg class="abs" style="left:1038px;top:136px" width="18" height="18" viewBox="0 0 18 18"><circle cx="7" cy="7" r="5.5" fill="none" stroke="#fff" stroke-width="2.5"/><line x1="11" y1="11" x2="16" y2="16" stroke="#fff" stroke-width="3"/></svg>
<svg class="abs" style="left:1084px;top:136px" width="20" height="18" viewBox="0 0 20 18"><path d="M0 1h4l3 10h10l2-7H6" fill="none" stroke="#fff" stroke-width="2.5"/><circle cx="8" cy="15" r="2" fill="#fff"/><circle cx="16" cy="15" r="2" fill="#fff"/></svg>

<!-- hero -->
<div class="abs hero" role="img" aria-label="Close-up photo of a rebuilt alternator beside a green engine part"></div>
<h1 class="abs hero-title">STARTERS &amp; ALTERNATORS</h1>
<p class="abs hero-sub">We sell and rebuild starters and alternators.</p>
<div class="abs btn" style="left:89px;top:460px;height:46px">SHOP NOW
  <svg width="20" height="18" viewBox="0 0 20 18"><path d="M0 1h4l3 10h10l2-7H6" fill="none" stroke="#fff" stroke-width="2.5"/><circle cx="8" cy="15" r="2" fill="#fff"/><circle cx="16" cy="15" r="2" fill="#fff"/></svg>
</div>

<!-- services -->
<h2 class="abs section-title" style="top:856px">SERVICES AND PRODUCTS OFFERED</h2>

<svg class="abs" style="left:33px;top:1111px" width="24" height="24" viewBox="0 0 24 24"><circle cx="12" cy="12" r="12" fill="var(--blue)"/><path d="M14 6l-6 6 6 6M8 12h10" stroke="#fff" stroke-width="2.6" fill="none"/></svg>
<svg class="abs" style="left:1131px;top:1110px" width="24" height="24" viewBox="0 0 24 24"><circle cx="12" cy="12" r="12" fill="var(--blue)"/><path d="M10 6l6 6-6 6M16 12H6" stroke="#fff" stroke-width="2.6" fill="none"/></svg>

<div class="abs service" style="left:108px;top:958px">
  <div class="service-icon" role="img" aria-label="Circular-arrow illustration of alternator terminals"></div>
  <div class="service-name">HIGH OUTPUT<br>ALTERNATORS</div>
  <p class="service-text">Lorem ipsum dolor sit amet, consectetur adipiscing elit. Nulla volutpat dui sit amet</p>
</div>
<div class="abs service" style="left:351px;top:958px">
  <div class="service-icon" role="img" aria-label="Circular-arrow illustration of a battery"></div>
  <div class="service-name">ORVAN<br>BATTERIES</div>
  <p class="service-text">Lorem ipsum dolor sit amet, consectetur adipiscing elit. Nulla volutpat dui sit amet</p>
</div>
<div class="abs service" style="left:610px;top:958px">
  <div class="service-icon" role="img" aria-label="Circular-arrow illustration of a toolbox with a check mark"></div>
  <div class="service-name">TROUBLE<br>SHOOTING TIPS</div>
  <p class="service-text">Lorem ipsum dolor sit amet, consectetur adipiscing elit. Nulla volutpat dui sit amet</p>
</div>
<div class="abs service" style="left:876px;top:958px">
  <div class="service-icon" role="img" aria-label="Circular-arrow illustration of a lightning bolt"></div>
  <div class="service-name">CURRENT<br>SPECIALS</div>
  <p class="service-text">Lorem ipsum dolor sit amet, consectetur adipiscing elit. Nulla volutpat dui sit amet</p>
</div>

<!-- about -->
<section class="abs about"></section>
<h2 class="abs about-title">ABOUT US</h2>
<p class="abs about-text">Lorem ipsum dolor sit amet, consectetur adipiscing elit. Nulla volutpat dui sit amet varius iaculis. Duis ut sapien in nibh aliquet pellentesque. Vivamus ex tellus, elementum at turpis sit amet, ullamcorper pharetra libero. In rutrum eros non leo dictum maximus volutpat ut odio. Sed id nibh dictum, aliquet lectus nec. cursus urna. Phasellus scelerisque urna sed nunc volutpat, vitae blandit mi auctor. Fusce egestas nec tellus eu blandit.</p>
<div class="abs btn" style="left:91px;top:1791px;height:48px">READ MORE
  <svg width="18" height="18" viewBox="0 0 18 18"><circle cx="9" cy="9" r="9" fill="#fff"/><path d="M7 4l5 5-5 5" stroke="var(--red)" stroke-width="2.6" fill="none"/></svg>
</div>
<div class="abs about-photo" role="img" aria-label="Photo of a workshop bench with a vise and blue air hose"></div>

<!-- product -->
<div class="abs product-box"></div>
<div class="abs product-photo" role="img" aria-label="Product photo of a grey electric motor"></div>
<h2 class="abs product-heading">OUR PRODUCT</h2>
<h3 class="abs product-name">NEQUE PORRO QUISQUAM</h3>
<div class="abs product-price">$80.00</div>
<p class="abs product-text">Lorem ipsum dolor sit amet, consectetur adipiscing elit. Nulla volutpat dui sit amet varius iaculis. Duis ut sapien in nibh aliquet pellentesque. Vivamus ex tellus, elementum at turpis sit amet, ullamcorper pharetra libero. In rutrum eros non leo dictum maximus volutpat ut odio.</p>
<div class="abs btn" style="left:544px;top:2327px;height:49px;padding:0 26px">ADD TO CART
  <svg width="20" height="18" viewBox="0 0 20 18"><path d="M0 1h4l3 10h10l2-7H6" fill="none" stroke="#fff" stroke-width="2.5"/><circle cx="8" cy="15" r="2" fill="#fff"/><circle cx="16" cy="15" r="2" fill="#fff"/></svg>
</div>

<!-- news -->
<section class="abs news"></section>
<h2 class="abs section-title" style="top:2530px">OUR LATEST NEWS</h2>
<p class="abs news-intro">Lorem ipsum dolor sit amet, consectetur adipiscing elit. Donec sapien sapien, molestie ac convallis vitae.</p>

<div class="abs news-main" role="img" aria-label="Photo of hands fitting a rotor into a starter on a workbench"></div>
<div class="abs news-main-bar">
  <div class="news-main-title">Lorem ipsum dolor sit amet</div>
  <div class="news-main-meta">&#128197;&nbsp; 12/04/2019 &nbsp;&nbsp;|&nbsp; 16 min Read . By&nbsp; Marek</div>
  <div class="arrow-btn" style="left:389px"><svg width="30" height="30" viewBox="0 0 30 30"><path d="M17 10l-5 5 5 5" stroke="#222" stroke-width="2.5" fill="none"/></svg></div>
  <div class="arrow-btn" style="left:430px"><svg width="30" height="30" viewBox="0 0 30 30"><path d="M13 10l5 5-5 5" stroke="#222" stroke-width="2.5" fill="none"/></svg></div>
</div>

<div class="abs news-thumb" style="left:603px;top:2690px;background:linear-gradient(135deg,#2f4a5a,#707a80 60%,#2a5a3a)" role="img" aria-label="Photo of a gloved hand working on starter parts"></div>
<div class="abs news-meta" style="left:816px;top:2706px">&#128197; 12/04/2019 &nbsp;|&nbsp; 16 min Read . By&nbsp; Marek</div>
<div class="abs news-title" style="left:816px;top:2735px">Lorem ipsum dolor sit</div>
<p class="abs news-text" style="left:816px;top:2771px">Lorem ipsum dolor sit amet, consectetur adipiscing elit. Donec sapien sapien, molestie ac convallis vitae, gravida ut ex.</p>
<div class="abs read-more" style="left:815px;top:2848px">Read More</div>

<div class="abs news-thumb" style="left:603px;top:2906px;background:linear-gradient(135deg,#c9d4dc,#4d7f98 55%,#2b4f66)" role="img" aria-label="Photo of a blue industrial motor"></div>
<div class="abs news-meta" style="left:818px;top:2922px">&#128197; 12/04/2019 &nbsp;|&nbsp; 16 min Read . By&nbsp; Marek</div>
<div class="abs news-title" style="left:818px;top:2952px">Lorem ipsum dolor sit</div>
<p class="abs news-text" style="left:818px;top:2989px">Lorem ipsum dolor sit amet, consectetur adipiscing elit. Donec sapien sapien, molestie ac convallis vitae, gravida ut ex.</p>
<div class="abs read-more" style="left:817px;top:3066px">Read More</div>

<!-- footer -->
<footer class="abs footer"></footer>
<div class="abs f-title">STAY UPDATED</div>
<div class="abs f-input"><span>ENTER THE EMAIL</span><div class="f-sub">SUBSCRIBE</div></div>
<div class="abs social"><i></i><i></i><i></i><i></i><i></i></div>
<div class="abs f-links">Home<br>About Us<br>Services<br>Our Product<br>Blog<br>Contact Us</div>
<div class="abs f-address">4170 Keawe Harbor Rd,<br>Kalaniwa, HI 96899.<br>555-014-2270<br>info@vellumtorq.com</div>
<div class="abs f-mark">VELLUMTORQ<br>REBUILDERS</div>
<div class="abs copy">© 2019 Copyrights&nbsp; Starters &amp;&nbsp; Alternators.| All Rights Reserved</div>
<div class="abs pay"><i></i><i></i><i></i><i></i><i></i><i></i></div>
<div class="abs policy"><span>Policy</span><span>Returns</span><span style="margin-left:18px">c32</span></div>

</body>
</html>
```